New Alcoholic Spiked Seltzer Line

We need a can design for a line of low calorie alcoholic seltzer. This product is a sparkling water and vodka drink with no sugar added in a slim 12 oz can.

This is a lighter, healthier, alternative to the sugary ready-to-drinks on the market. The product contains only 3 ingredients: Vodka, Water and Natural Flavors. It has only 100 calories but still has 5% alcohol, so you don't need to sacrifice alcohol to cut calories.

This product also does not contain any preservatives.

We want this design to communicate the following objectives to the consumer and in this order:

1. Appetizing product
2.Low calorie
3.Communicate the type of beverage (Spiked Seltzer)

The brand name of the product is VELKA.

The flavor of the product needed to be used for the design is Mango-Orange.

Comparable products are:

www.brisavelfizz.example/
https://www.tarnowbubble.example
https://quellrind.example/

The designs should not infringe or copy the creative directions of the products mentionned above. They are only given so that you can better understand the type of product we are developing.

Target Market(s)

Young Professional women between the ages of 25 and 44

Industry/Entity Type

Product

Colors

Designer to choose colors to be used in the design.

Requirements
Must have
• Design extendibility, meaning it can be adapted for other flavors.
• This is a new category in the market we are targeting, so consumers must easily be able to identify what type of product this is.

```html
<!DOCTYPE html>
<html lang="en">
<head>
<meta charset="utf-8">
<title>VELKA Mango &amp; Orange Spiked Seltzer – Can Label</title>
<link rel="stylesheet" href="https://fonts.googleapis.com/css2?family=Montserrat:wght@500;700;800&family=Nunito:wght@500;600&display=swap">
<style>
  :root {
    --backdrop: #f0c27f;
    --can-white: #f7f6f4;
    --can-shade: #e4e2de;
    --rim: #c9cbcd;
    --rim-dark: #9ea1a4;
    --orange-deep: #d2691e;
    --orange: #e8893a;
    --orange-light: #f3b06a;
    --yellow: #e3b23c;
    --bubble: #f3e2d0;
    --text-light: #ffffff;
  }
  * { margin: 0; padding: 0; box-sizing: border-box; }
  html, body {
    width: 1200px;
    height: 1200px;
    overflow: hidden;
    background: var(--backdrop);
  }
  .stage {
    width: 1200px;
    height: 1200px;
    display: flex;
    align-items: center;
    justify-content: center;
  }
  .can-label { display: block; }
  .brand-name {
    font-family: "Montserrat", sans-serif;
    font-weight: 800;
    font-size: 118px;
    letter-spacing: 4px;
    fill: var(--orange);
  }
  .badge-arc {
    font-family: "Montserrat", sans-serif;
    font-weight: 700;
    font-size: 15px;
    letter-spacing: 5px;
    fill: var(--text-light);
  }
  .badge-number {
    font-family: "Montserrat", sans-serif;
    font-weight: 800;
    font-size: 58px;
    fill: var(--text-light);
  }
  .badge-unit {
    font-family: "Montserrat", sans-serif;
    font-weight: 700;
    font-size: 17px;
    fill: var(--text-light);
  }
  .flavor-name {
    font-family: "Montserrat", sans-serif;
    font-weight: 700;
    font-size: 58px;
    fill: var(--text-light);
  }
  .flavor-description {
    font-family: "Nunito", sans-serif;
    font-weight: 600;
    font-size: 22px;
    letter-spacing: 1.5px;
    fill: var(--text-light);
  }
  .spec-small {
    font-family: "Nunito", sans-serif;
    font-weight: 600;
    font-size: 13px;
    fill: var(--text-light);
  }
  .spec-value {
    font-family: "Nunito", sans-serif;
    font-weight: 600;
    font-size: 22px;
    fill: var(--text-light);
  }
</style>
</head>
<body>
<main class="stage">
  <svg class="can-label" width="480" height="1120" viewBox="0 0 480 1120" xmlns="http://www.w3.org/2000/svg">
    <defs>
      <linearGradient id="body-white" x1="0" x2="1" y1="0" y2="0">
        <stop offset="0" stop-color="var(--can-shade)"/>
        <stop offset="0.35" stop-color="var(--can-white)"/>
        <stop offset="0.75" stop-color="var(--can-white)"/>
        <stop offset="1" stop-color="var(--can-shade)"/>
      </linearGradient>
      <linearGradient id="body-orange" x1="0" x2="1" y1="0" y2="0">
        <stop offset="0" stop-color="var(--orange)"/>
        <stop offset="0.45" stop-color="var(--orange-deep)"/>
        <stop offset="0.8" stop-color="var(--orange-light)"/>
        <stop offset="1" stop-color="var(--orange)"/>
      </linearGradient>
      <linearGradient id="badge-fill" x1="0" x2="0" y1="0" y2="1">
        <stop offset="0" stop-color="var(--orange)"/>
        <stop offset="1" stop-color="var(--yellow)"/>
      </linearGradient>
      <linearGradient id="rim-metal" x1="0" x2="1" y1="0" y2="0">
        <stop offset="0" stop-color="var(--rim-dark)"/>
        <stop offset="0.5" stop-color="#eceeef"/>
        <stop offset="1" stop-color="var(--rim-dark)"/>
      </linearGradient>
      <clipPath id="can-body">
        <rect x="20" y="70" width="440" height="980" rx="14"/>
      </clipPath>
      <path id="arc-top" d="M 150 250 A 90 90 0 0 1 330 250"/>
      <path id="arc-bottom" d="M 140 250 A 100 100 0 0 0 340 250"/>
    </defs>

    <!-- top rim -->
    <path class="can-top-rim" d="M 60 20 H 420 Q 430 20 432 30 L 460 70 H 20 L 48 30 Q 50 20 60 20 Z" fill="url(#rim-metal)"/>
    <!-- bottom rim -->
    <path class="can-bottom-rim" d="M 20 1050 H 460 L 436 1094 Q 432 1102 420 1102 H 60 Q 48 1102 44 1094 Z" fill="url(#rim-metal)"/>

    <g clip-path="url(#can-body)">
      <rect x="20" y="70" width="440" height="980" fill="url(#body-white)"/>

      <!-- bubbles -->
      <g class="bubbles" fill="var(--bubble)" opacity="0.7">
        <circle cx="90" cy="110" r="46"/>
        <circle cx="420" cy="200" r="40"/>
        <circle cx="70" cy="330" r="22"/>
        <circle cx="110" cy="460" r="18"/>
        <circle cx="420" cy="480" r="26"/>
        <circle cx="60" cy="720" r="30"/>
        <circle cx="140" cy="730" r="14"/>
      </g>

      <!-- orange lower band with wave -->
      <path class="flavor-band" d="M 20 860 C 100 830 120 770 230 760 C 340 750 400 770 460 740 V 1050 H 20 Z" fill="url(#body-orange)"/>
    </g>

    <!-- calorie badge -->
    <g class="calorie-badge">
      <circle cx="240" cy="250" r="112" fill="url(#badge-fill)"/>
      <rect x="188" y="320" width="104" height="110" fill="url(#badge-fill)"/>
      <circle cx="240" cy="440" r="72" fill="var(--yellow)"/>
      <text class="badge-arc"><textPath href="#arc-top" startOffset="50%" text-anchor="middle">LOW CALORIE</textPath></text>
      <text class="badge-arc"><textPath href="#arc-bottom" startOffset="50%" text-anchor="middle">SPIKED SELTZER</textPath></text>
      <text class="badge-number" x="240" y="262" text-anchor="middle">100</text>
      <text class="badge-unit" x="240" y="288" text-anchor="middle">CALORIES</text>
      <circle cx="240" cy="450" r="34" fill="var(--orange-light)" role="img" aria-label="Small mango and orange slice icon"/>
    </g>

    <!-- brand name -->
    <text class="brand-name" x="240" y="650" text-anchor="middle">VELKA</text>

    <!-- flavor -->
    <text class="flavor-name" x="50" y="880">MANGO &amp;</text>
    <text class="flavor-name" x="50" y="942">ORANGE</text>
    <text class="flavor-description" x="50" y="990">Sparkling water and vodka</text>
    <text class="flavor-description" x="50" y="1018">drink with no sugar added</text>

    <text class="spec-small" x="50" y="1000" dy="0" visibility="hidden">ALC</text>
    <g class="can-specs">
      <text class="spec-small" x="380" y="1010" text-anchor="end" visibility="hidden"></text>
    </g>
    <text class="spec-small" x="52" y="1032" dy="0"></text>
    <g class="alcohol-spec">
      <text class="spec-small" x="40" y="1025" visibility="hidden"></text>
    </g>
    <text class="spec-small" x="36" y="1034"></text>
  </svg>
</main>
</body>
</html>
```